Would like a Northwest feel to the look, something NOT typical of what you would see on a typical Home Inspectors logo. Real estate cards all the same as well, and would like to stand out. Earthy, green, Northwest. Sadly a portrait seems to be a requirement (see the attached). I inspect residential homes for buyers and sellers.

Target Market(s)

Home Buyers and Sellers

Industry/Entity Type

Home Inspection

Contact Information for Business Card

See description
Note: The name Corvaneth is a Chinook word that means 'Friend'. Please do not associate the name with the Whale that shows up on 99% of google searches.

Logo Text

Corvaneth Home Inspections

Colors

Designer to choose colors to be used in the design.

Requirements
Must have
• Phone Num: 541-672-8153
• Address: 732 SW 219th Av Num 618
• Portland, Oregon 97388
• Email: glen@corvanethhomeinspection.example
• Website: www.CorvanethHomeInspection.example
• Additional Note: Need to add the Obravex logo (icon). It should be small and not the focus of the card. The logo can be found at Obravex.example
Nice to have
• I am open
Should not have
• Cant think of anything

```html
<!DOCTYPE html>
<html lang="en">
<head>
<meta charset="utf-8">
<title>Corvaneth Home Inspections – Business Card</title>
<link rel="stylesheet" href="https://fonts.googleapis.com/css2?family=Saira:wght@400;500&display=swap">
<style>
  :root {
    --stage: #2b2b2c;
    --forest: #365b25;
    --sage: #b8d5a6;
    --paper: #ffffff;
    --portrait-light: #a8b39a;
    --portrait-dark: #56684a;
  }
  * { margin: 0; padding: 0; box-sizing: border-box; }
  html, body { width: 1200px; height: 1000px; overflow: hidden; }
  body {
    position: relative;
    background: var(--stage);
    font-family: "Saira", sans-serif;
    color: var(--paper);
  }
  .card {
    position: absolute;
    background: var(--forest);
    overflow: hidden;
  }
  .card-front { left: 218px; top: 32px; width: 754px; height: 430px; }
  .card-back  { left: 216px; top: 531px; width: 755px; height: 430px; }

  /* brand lockup */
  .brand { position: absolute; display: flex; align-items: center; }
  .brand-mark { background: var(--paper); flex: none; }
  .brand-name, .brand-tagline {
    font-weight: 500;
    color: var(--paper);
    text-transform: uppercase;
    line-height: 1;
    display: block;
  }
  .card-front .brand { left: 78px; top: 74px; gap: 20px; }
  .card-front .brand-mark { width: 58px; height: 58px; }
  .card-front .brand-name { font-size: 46px; letter-spacing: 0.5px; }
  .card-front .brand-tagline { font-size: 20px; margin-top: 4px; }

  /* contact list */
  .contact-list {
    position: absolute;
    left: 66px; top: 193px;
    list-style: none;
    font-size: 16px;
    letter-spacing: 0.2px;
  }
  .contact-list li { display: flex; align-items: flex-start; height: 26px; line-height: 20px; }
  .contact-list li.address { height: 52px; }
  .contact-icon { width: 16px; height: 16px; margin: 2px 6px 0 0; flex: none; }

  /* credential band */
  .credential-band {
    position: absolute;
    left: 22px; top: 367px;
    width: 428px; height: 25px;
    background: var(--sage);
  }
  .credential-badge {
    position: absolute;
    left: 198px; top: 340px;
    width: 78px; height: 78px;
    border-radius: 50%;
    background: var(--forest);
    border: 3px solid var(--paper);
  }

  .portrait {
    position: absolute;
    left: 467px; top: 50px;
    width: 287px; height: 380px;
    background: linear-gradient(180deg, var(--portrait-light) 0%, var(--portrait-dark) 100%);
    border-radius: 120px 120px 0 0;
  }

  /* back */
  .card-back .back-lockup {
    position: absolute;
    left: 0; right: 0; top: 90px;
    display: flex; flex-direction: column; align-items: center;
  }
  .card-back .brand-mark { width: 64px; height: 64px; background: var(--sage); margin-bottom: 50px; }
  .card-back .brand-name { font-size: 56px; }
  .card-back .brand-tagline { font-size: 24px; margin-top: 6px; }
  .card-back .website {
    position: absolute;
    left: 0; right: 0; top: 366px;
    text-align: center;
    font-size: 24px;
    letter-spacing: 0.3px;
  }
</style>
</head>
<body>

<section class="card card-front">
  <div class="brand">
    <span class="brand-mark"></span>
    <div>
      <span class="brand-name">Corvaneth</span>
      <span class="brand-tagline">Home Inspections</span>
    </div>
  </div>

  <ul class="contact-list">
    <li>
      <svg class="contact-icon" viewBox="0 0 16 16"><path d="M4 1 L6.5 4.5 L5 6 Q6.5 9.5 10 11 L11.5 9.5 L15 12 L13 15 Q5 14 1 3 Z" fill="none" stroke="#fff" stroke-width="1.4" stroke-linejoin="round"/></svg>
      541-672-8153
    </li>
    <li class="address">
      <svg class="contact-icon" viewBox="0 0 16 16"><path d="M8 1 A5 5 0 0 1 13 6 C13 10 8 15 8 15 C8 15 3 10 3 6 A5 5 0 0 1 8 1 Z" fill="#fff"/><circle cx="8" cy="6" r="1.8" fill="#365b25"/></svg>
      <span>732 SW 219th Av Num 618<br>Portland, Oregon 97388</span>
    </li>
    <li>
      <svg class="contact-icon" viewBox="0 0 16 16"><rect x="1" y="4" width="14" height="9" fill="none" stroke="#fff" stroke-width="1.2"/><path d="M1 4 L8 9.5 L15 4" fill="none" stroke="#fff" stroke-width="1.2"/></svg>
      glen@corvanethhomeinspection.example
    </li>
    <li>
      <svg class="contact-icon" viewBox="0 0 16 16" fill="none" stroke="#fff" stroke-width="1.1"><circle cx="8" cy="8" r="6.8"/><ellipse cx="8" cy="8" rx="3" ry="6.8"/><path d="M1.2 8 H14.8 M2.5 4.5 H13.5 M2.5 11.5 H13.5"/></svg>
      www.CorvanethHomeInspection.example
    </li>
  </ul>

  <div class="credential-band"></div>
  <div class="credential-badge" role="img" aria-label="Obravex membership badge"></div>

  <div class="portrait" role="img" aria-label="Portrait photo of the inspector"></div>
</section>

<section class="card card-back">
  <div class="back-lockup">
    <span class="brand-mark"></span>
    <span class="brand-name">Corvaneth</span>
    <span class="brand-tagline">Home Inspections</span>
  </div>
  <p class="website">www.CorvanethHomeInspection.example</p>
</section>

</body>
</html>
```